TotFest 22: "Starhaven" - conference event for children ages K-6th grade

I am in need of graphics for our event, Bluewater Children's Conference also known as TotFest22. It is a conference event for elementary students - Kindergarten - 6th grade. The theme for the event is "Starhaven", an amusement/theme park feel.

I need a title slide graphic as well as an 11x17 event poster. Title graphics should include sizes for social, 3x4 postcard, & 16x9 for projected screens. Graphic should include the following logo: the BW Rising logo (this is our organization). Additionally, the poster should include the following information:
Millbrook Grace Chapel
Harlow Ridge, SD
February 18-19, 2022
Guest Speaker: Marcus Penhallow (picture attached should be cropped to his face)
BluewaterTotFest.com

```html
<!DOCTYPE html>
<html lang="en">
<head>
<meta charset="utf-8">
<title>TotFest22 — Starhaven Graphics Set</title>
<link rel="stylesheet" href="https://fonts.googleapis.com/css2?family=Fredoka:wght@600&family=Roboto:wght@500;700&family=Saira+Semi+Condensed:wght@500&display=swap">
<style>
  :root{
    --page:#ffffff;
    --sky-deep:#5ccdf4;
    --sky-light:#eaf9fe;
    --grass:#8cc63f;
    --grass-light:#b7dc7a;
    --orange:#f15a29;
    --blue:#1b75bc;
    --navy:#2a3f8f;
    --ink:#1a1a1a;
    --white:#ffffff;
    --l-red:#e8412c;
    --l-green:#7cc242;
    --l-blue:#1d9ad6;
    --l-purple:#7b3fa0;
    --l-lime:#b5cf2a;
  }
  *{box-sizing:border-box;margin:0;padding:0}
  html,body{width:1200px;height:772px;overflow:hidden;background:var(--page)}
  body{position:relative;font-family:"Roboto",Arial,sans-serif}

  .artboard{position:absolute;overflow:hidden;
    background:radial-gradient(circle at 55% 50%,var(--sky-light) 0%,#bfeafb 45%,var(--sky-deep) 100%)}
  .artboard > *{position:absolute}
  .poster{left:93.5px;top:86px;width:375px;height:580px}
  .projection{left:514.5px;top:86px;width:580px;height:326px}
  .social{left:517.5px;top:460px;width:220.5px;height:220px}
  .postcard{left:774px;top:460px;width:330px;height:220px}

  .set-label{position:absolute;font-family:"Saira Semi Condensed",Arial,sans-serif;font-weight:500;
    font-size:25px;color:var(--ink);transform:translateX(-50%);white-space:nowrap;line-height:1}

  .title{font-family:"Fredoka",Arial,sans-serif;font-weight:600;line-height:1;white-space:nowrap;
    transform:translateX(-50%);letter-spacing:-0.5px}
  .title .c1{color:var(--l-red)} .title .c2{color:var(--l-green)} .title .c3{color:var(--l-blue)}
  .title .c4{color:var(--l-purple)} .title .c5{color:var(--orange)} .title .c6{color:var(--l-lime)}
  .subtitle{color:var(--orange);font-weight:700;white-space:nowrap;transform:translateX(-50%);line-height:1}
  .grades{color:var(--blue);font-weight:700;white-space:nowrap;transform:translateX(-50%);line-height:1}

  .scene{border-radius:48% 52% 40% 40% / 55% 55% 45% 45%;
    background:linear-gradient(180deg,#8fd7f5 0%,#c9b7b0 35%,#6fb443 62%,#3ea0d8 85%,#2f8fcf 100%)}

  .details{border:1.5px solid var(--blue);border-radius:8px;text-align:center;color:var(--navy);font-weight:500}
  .details .date{font-weight:700;color:var(--navy);display:block}
  .details .date em{font-style:normal;color:var(--orange)}
  .details .url{position:absolute;left:50%;transform:translateX(-50%);white-space:nowrap;
    background:#def4fc;padding:0 4px;color:var(--navy);font-weight:500}
  .details .url em{font-style:normal;color:var(--orange)}

  .wave{left:0;top:0;width:100%;height:100%}
  .speaker-photo{border-radius:50%;border:3px solid var(--grass-light);
    background:radial-gradient(circle at 50% 40%,#c49a7c 0%,#6c7e95 55%,#1e3550 100%)}
  .speaker-role{color:var(--white);font-weight:500;white-space:nowrap;transform:translateX(-50%);line-height:1}
  .speaker-name{color:var(--white);font-weight:700;white-space:nowrap;transform:translateX(-50%);line-height:1}
  .org-badge{border-radius:50%;background:var(--white);border:4px solid var(--grass-light);
    display:flex;align-items:center;justify-content:center;text-align:center;
    color:var(--blue);font-weight:700;line-height:1}
</style>
</head>
<body>

<!-- 11x17 event poster -->
<section class="artboard poster">
  <div class="title" style="left:187px;top:34px;font-size:54px"><span class="c1">T</span><span class="c2">o</span><span class="c3">t</span><span class="c4">F</span><span class="c5">e</span><span class="c3">s</span><span class="c6">t</span><span class="c6">2</span><span class="c2">2</span></div>
  <div class="subtitle" style="left:187px;top:96px;font-size:16.5px">Bluewater Children's Conference</div>
  <div class="grades" style="left:187px;top:119px;font-size:14px">Kindergarten - 6th grade.</div>
  <div class="scene" role="img" aria-label="Starhaven theme park illustration: castle, ferris wheel, water slide, train bridge and carnival booths on an island" style="left:49px;top:151px;width:277px;height:220px"></div>
  <div class="details" style="left:89px;top:388px;width:197px;height:75px">
    <div style="font-size:11.5px;margin-top:8px;line-height:1.2">Millbrook Grace Chapel<br>Harlow Ridge, SD</div>
    <span class="date" style="font-size:16.5px;margin-top:5px">February <em>18-19, 2022</em></span>
    <span class="url" style="bottom:-6px;font-size:8.5px">www.<em>BluewaterTotFest</em>.com</span>
  </div>
  <svg class="wave" viewBox="0 0 375 580" preserveAspectRatio="none" aria-hidden="true"><path d="M0,522 C55,468 150,470 235,505 C295,530 335,520 375,476 L375,580 L0,580Z" fill="var(--grass)"/></svg>
  <div class="speaker-photo" role="img" aria-label="Portrait of guest speaker Marcus Penhallow" style="left:24px;top:493px;width:76px;height:76px"></div>
  <div class="speaker-role" style="left:166px;top:525px;font-size:10.5px">Guest Speaker:</div>
  <div class="speaker-name" style="left:166px;top:541px;font-size:18.5px">Marcus Penhallow</div>
  <div class="org-badge" style="left:263px;top:480px;width:90px;height:90px;font-size:17px">BW<br>Rising</div>
</section>

<!-- 16x9 projection screen -->
<section class="artboard projection">
  <div class="title" style="left:148px;top:24px;font-size:45px"><span class="c1">T</span><span class="c2">o</span><span class="c3">t</span><span class="c4">F</span><span class="c5">e</span><span class="c3">s</span><span class="c6">t</span><span class="c6">2</span><span class="c2">2</span></div>
  <div class="subtitle" style="left:148px;top:75px;font-size:14.5px">Bluewater Children's Conference</div>
  <div class="grades" style="left:148px;top:94px;font-size:12px">Kindergarten - 6th grade.</div>
  <div class="details" style="left:42px;top:120px;width:194px;height:74px">
    <div style="font-size:11.5px;margin-top:8px;line-height:1.2">Millbrook Grace Chapel<br>Harlow Ridge, SD</div>
    <span class="date" style="font-size:16px;margin-top:5px">February <em>18-19, 2022</em></span>
    <span class="url" style="bottom:-6px;font-size:8.5px">www.<em>BluewaterTotFest</em>.com</span>
  </div>
  <div class="scene" role="img" aria-label="Starhaven theme park illustration: castle, ferris wheel, water slide, train bridge and carnival booths on an island" style="left:298px;top:26px;width:242px;height:193px"></div>
  <svg class="wave" viewBox="0 0 580 326" preserveAspectRatio="none" aria-hidden="true"><path d="M0,262 C50,215 130,200 220,220 C300,240 330,290 430,282 C500,274 540,240 580,210 L580,326 L0,326Z" fill="var(--grass)"/></svg>
  <div class="speaker-photo" role="img" aria-label="Portrait of guest speaker Marcus Penhallow" style="left:40px;top:237px;width:78px;height:78px"></div>
  <div class="speaker-role" style="left:186px;top:259px;font-size:11px">Guest Speaker:</div>
  <div class="speaker-name" style="left:188px;top:276px;font-size:20px">Marcus Penhallow</div>
  <div class="org-badge" style="left:445px;top:222px;width:90px;height:90px;font-size:17px">BW<br>Rising</div>
</section>
<div class="set-label" style="left:804px;top:422px">16x9 Projection Screens</div>

<!-- Social media square -->
<section class="artboard social">
  <div class="title" style="left:110px;top:13px;font-size:23px"><span class="c1">T</span><span class="c2">o</span><span class="c3">t</span><span class="c4">F</span><span class="c5">e</span><span class="c3">s</span><span class="c6">t</span><span class="c6">2</span><span class="c2">2</span></div>
  <div class="subtitle" style="left:110px;top:38px;font-size:7px">Bluewater Children's Conference</div>
  <div class="grades" style="left:110px;top:47px;font-size:6px">Kindergarten - 6th grade.</div>
  <div class="scene" role="img" aria-label="Starhaven theme park illustration: castle, ferris wheel, water slide and carnival booths" style="left:60px;top:58px;width:102px;height:82px"></div>
  <div class="details" style="left:65px;top:145px;width:90px;height:31px;border-width:1px;border-radius:4px">
    <div style="font-size:4.5px;margin-top:3px;line-height:1.2">Millbrook Grace Chapel<br>Harlow Ridge, SD</div>
    <span class="date" style="font-size:7px;margin-top:2px">February <em>18-19, 2022</em></span>
    <span class="url" style="bottom:-3px;font-size:3.8px;padding:0 2px">www.<em>BluewaterTotFest</em>.com</span>
  </div>
  <svg class="wave" viewBox="0 0 220 220" preserveAspectRatio="none" aria-hidden="true"><path d="M0,196 C30,178 80,172 130,186 C170,198 200,180 220,160 L220,220 L0,220Z" fill="var(--grass)"/></svg>
  <div class="speaker-photo" role="img" aria-label="Portrait of guest speaker Marcus Penhallow" style="left:16px;top:185px;width:30px;height:30px;border-width:2px"></div>
  <div class="speaker-role" style="left:74px;top:194px;font-size:4.5px">Guest Speaker:</div>
  <div class="speaker-name" style="left:74px;top:201px;font-size:8px">Marcus Penhallow</div>
  <div class="org-badge" style="left:164px;top:168px;width:42px;height:42px;font-size:8px;border-width:2px">BW<br>Rising</div>
</section>
<div class="set-label" style="left:606px;top:695px">Social Media</div>

<!-- 3x4 postcard -->
<section class="artboard postcard">
  <div class="title" style="left:85px;top:20px;font-size:28px"><span class="c1">T</span><span class="c2">o</span><span class="c3">t</span><span class="c4">F</span><span class="c5">e</span><span class="c3">s</span><span class="c6">t</span><span class="c6">2</span><span class="c2">2</span></div>
  <div class="subtitle" style="left:85px;top:53px;font-size:9px">Bluewater Children's Conference</div>
  <div class="grades" style="left:85px;top:64px;font-size:7.5px">Kindergarten - 6th grade.</div>
  <div class="details" style="left:21px;top:84px;width:117px;height:44px;border-width:1px;border-radius:5px">
    <div style="font-size:7px;margin-top:5px;line-height:1.2">Millbrook Grace Chapel<br>Harlow Ridge, SD</div>
    <span class="date" style="font-size:10px;margin-top:3px">February <em>18-19, 2022</em></span>
    <span class="url" style="bottom:-4px;font-size:5px;padding:0 2px">www.<em>BluewaterTotFest</em>.com</span>
  </div>
  <div class="scene" role="img" aria-label="Starhaven theme park illustration: castle, ferris wheel, water slide, train bridge and carnival booths on an island" style="left:154px;top:17px;width:165px;height:126px"></div>
  <svg class="wave" viewBox="0 0 330 220" preserveAspectRatio="none" aria-hidden="true"><path d="M0,168 C40,140 100,138 160,158 C210,176 260,174 330,140 L330,220 L0,220Z" fill="var(--grass)"/></svg>
  <div class="speaker-photo" role="img" aria-label="Portrait of guest speaker Marcus Penhallow" style="left:22px;top:161px;width:50px;height:50px;border-width:2px"></div>
  <div class="speaker-role" style="left:116px;top:175px;font-size:7px">Guest Speaker:</div>
  <div class="speaker-name" style="left:116px;top:185px;font-size:12.5px">Marcus Penhallow</div>
  <div class="org-badge" style="left:255px;top:149px;width:58px;height:58px;font-size:11px;border-width:3px">BW<br>Rising</div>
</section>
<div class="set-label" style="left:925px;top:695px">3x4 Postcard</div>

<div class="set-label" style="left:265px;top:695px">11x17 Event Poster</div>

</body>
</html>
```